Online Cooking App Pitch Deck- (THIS IS NOT A FOOD BUSINESS OR FOOD SERVICE, NO FOOD PICTURES)

Project Goal:
Design a visually compelling pitch deck to be used for securing investment. Looking for the pitch deck to be about the design using shapes, colors, fonts and sizes. Must be creative yet simple and clean.
Color Palette:
https://palettrix.example/ff3800-ffe2db-fefefa-2d3e50-010b13

(We want most screens to use #FEFEFA)

This is the current pitch deck we need simplified and redesigned (USE TEXT IN THE GOOGLE LINK TO SHOW IN YOUR DESIGN):

https://slides.vornidex.example/deck/8QmTzR42kLpWx7nHa3Jv-cYdoeBtfGuqN/edit?share=link&uid=592031846720518390417&fmt=true&mode=true

Project is now guaranteed. Remember use the text in the google link in powerpoint design. Use a little more color not just the logo color. Do not use any pictures of food this is not food related business. We care more about style and design of shapes, text, color fonts.

Target Market(s)

Investors (venture capitalists, angel investors) interested in innovative technology solutions within the food industry.

Font styles to use
Serif
Sans Serif

Requirements
Nice to have
• Simple, abstract background non distracting but complementary.
Should not have
• No pictures

```html
<!DOCTYPE html>
<html lang="en">
<head>
<meta charset="utf-8">
<title>Stovewise — Investor Deck Overview</title>
<link href="https://fonts.googleapis.com/css2?family=Poppins:wght@600;700;800&family=Montserrat:wght@400;500;600&display=swap" rel="stylesheet">
<style>
:root{
  --stage:#e8e8ea;
  --night:#0b0b10;
  --ember:#ff3800;
  --paper:#fefefa;
  --mist:#f2f2f4;
  --stone:#dcdcde;
  --ink:#1f1f24;
  --violet:#d000d0;
  --grey-text:#8a8a90;
}
*{margin:0;padding:0;box-sizing:border-box}
html,body{width:1200px;height:1200px;overflow:hidden;background:var(--stage)}
body{position:relative;font-family:"Montserrat",sans-serif;color:var(--ink)}
.slide{position:absolute;width:346px;height:194px;overflow:hidden;background:var(--mist)}
.slide--dark{background:var(--night);color:var(--paper)}
.slide--light{background:var(--mist)}
.col-1{left:49px}.col-2{left:428px}.col-3{left:811px}
.row-1{top:48px}.row-2{top:278px}.row-3{top:499px}.row-4{top:733px}.row-5{top:966px}
.rail{position:absolute;left:0;top:0;bottom:0;width:23px;background:var(--paper)}
.tagline{position:absolute;left:11px;bottom:68px;transform:rotate(-90deg);transform-origin:left bottom;font-size:3.4px;letter-spacing:.9px;color:var(--violet);white-space:nowrap;width:60px}
.page-no{position:absolute;left:10px;bottom:10px;font-size:3px;color:var(--grey-text)}
.confidential{position:absolute;right:46px;bottom:8px;font-size:3.2px;color:var(--grey-text)}
.brand-mark{position:absolute;right:10px;bottom:7px;font-family:"Poppins",sans-serif;font-weight:700;font-size:5px;color:var(--ember)}
.headline{font-family:"Poppins",sans-serif;font-weight:800;line-height:1.02}
.accent{color:var(--ember)}
.copy{font-size:4.3px;line-height:1.72;color:var(--ink)}
.kicker{font-family:"Poppins",sans-serif;font-weight:600;font-size:6.4px;color:var(--ink)}
.divider-v{position:absolute;width:.6px;background:var(--violet)}
.divider-h{position:absolute;height:.6px;background:var(--violet)}

/* cover */
.cover-brand{position:absolute;left:21px;top:20px;font-family:"Poppins",sans-serif;font-weight:600;font-size:10px}
.cover-title{position:absolute;left:68px;top:86px;font-size:23.5px;color:var(--ember)}
.cover-sub{position:absolute;left:68px;top:141px;font-size:4.6px}
.cover-foot{position:absolute;left:68px;bottom:8px;font-size:3.2px}
.slide--dark .cover-brand{color:var(--paper)}
.slide--light .cover-brand{color:#a8a8ad}
.slide--light .cover-sub,.slide--light .cover-foot{color:#444}

/* hero */
.hero-brand{position:absolute;left:46px;top:69px;font-family:"Poppins",sans-serif;font-weight:800;font-size:10.5px;color:var(--ember)}
.hero-title{position:absolute;left:46px;top:84px;font-size:24px;color:var(--night);line-height:1.1}
.hero-photo{position:absolute;right:0;top:0;width:170px;height:194px;background:linear-gradient(125deg,rgba(232,232,234,0) 0%,#d9cfc2 35%,#8c6a55 60%,#3b2a22 100%)}
.hero-fade{position:absolute;left:0;top:0;width:210px;height:194px;background:linear-gradient(90deg,#dcdcde 70%,rgba(220,220,222,0))}

/* about */
.about-left{position:absolute;left:0;top:0;width:199px;height:194px;background:var(--stone)}
.about-title{position:absolute;left:31px;top:18px;font-size:13.5px}
.about-panel{position:absolute;left:199px;top:0;right:0;height:194px;background:var(--ember);color:var(--paper)}
.about-panel .copy{position:absolute;left:21px;top:42px;width:104px;color:var(--paper)}
.about-panel .confidential{color:#ffe2db}
.about-panel .brand-mark{color:var(--paper)}

/* section dividers */
.section-title{position:absolute;right:34px;text-align:right;color:var(--ember)}

/* insights */
.insight-kicker{position:absolute;left:31px;top:17px}
.insight-title{position:absolute;right:141px;text-align:right;font-size:18.5px;color:var(--ink)}
.insight-body{position:absolute;left:219px;width:118px}

/* problem list */
.problem-panel{position:absolute;left:162px;top:0;right:0;height:168px;background:var(--mist)}
.problem-item{position:absolute;left:30px;width:118px;padding-left:13px}
.problem-item::before{content:"";position:absolute;left:0;top:1px;width:6.5px;height:6.5px;border-radius:50%;background:var(--violet)}
.problem-title{position:absolute;left:35px;top:99px;font-size:24px;color:var(--ember)}

/* consumer insight */
.ci-top{position:absolute;left:23px;top:0;right:0;height:86px;background:var(--paper)}
.ci-kicker{position:absolute;left:31px;top:17px}
.ci-title{position:absolute;left:31px;top:32px;font-size:17.3px;line-height:1.16}
.ci-body{position:absolute;left:118px;top:99px;width:194px}

/* landscape */
.comp-col{position:absolute;top:0;width:107px;height:139px;background:var(--mist);padding:11px 12px 0}
.comp-name{height:24px;font-family:"Poppins",sans-serif;font-weight:700;font-size:9px;color:var(--ink);display:flex;align-items:center;gap:4px}
.comp-name .dot{width:8px;height:8px;background:var(--night)}
.comp-copy{font-size:3.4px;line-height:1.7;color:var(--violet);margin-top:5px;height:55px}
.comp-label{font-size:3.6px;font-weight:600;color:var(--ink);margin-top:8px}
.comp-value{font-family:"Poppins",sans-serif;font-weight:700;font-size:12px;color:var(--violet);line-height:1.3}
.takeaway{position:absolute;left:41px;top:154px;width:270px;font-size:3.7px;line-height:1.75}
.takeaway b{color:var(--ember);font-weight:600}
</style>
</head>
<body>

<section class="slide slide--dark col-1 row-1">
  <div class="cover-brand">Stovewise</div>
  <div class="tagline" style="left:26px;bottom:50px">Cook. Learn. Repeat.</div>
  <h1 class="headline cover-title">Investor<br>Overview</h1>
  <p class="cover-sub">This document exists for our future partners.</p>
  <p class="cover-foot">Proprietary and Confidential</p>
</section>

<section class="slide slide--light col-2 row-1">
  <div class="cover-brand">Stovewise</div>
  <div class="tagline" style="left:26px;bottom:50px">Cook. Learn. Repeat.</div>
  <h1 class="headline cover-title">Investor<br>Overview</h1>
  <p class="cover-sub">This document exists for our future partners.</p>
  <p class="cover-foot">Proprietary and Confidential</p>
</section>

<section class="slide col-3 row-1" style="background:var(--stone)">
  <div class="hero-photo" role="img" aria-label="Photo of a smartphone showing the app with a couple cooking together"></div>
  <div class="hero-fade"></div>
  <div class="tagline">Cook. Learn. Repeat.</div>
  <div class="page-no">2</div>
  <div class="hero-brand">STOVEWISE</div>
  <h2 class="headline hero-title">A New<br>Cooking<br>Platform</h2>
</section>

<section class="slide col-1 row-2">
  <div class="about-left"></div>
  <div class="tagline">Cook. Learn. Repeat.</div>
  <div class="page-no">3</div>
  <h2 class="headline about-title">What is<br><span class="accent">STOVEWISE ?</span></h2>
  <div class="about-panel">
    <p class="copy">Lorem ipsum dolor sit amet, consectetur adipiscing elit, sed do eiusmod tempor incididunt ut labore et dolore magna aliqua. Ut enim ad minim veniam, quis nostrud exercitation ullamco laboris nisi ut aliquip ex ea commodo consequat. Duis aute irure dolor in reprehenderit in voluptate velit esse cillum dolore eu fugiat nulla pariatur. Excepteur sint occaecat cupidatat non proident, sunt in culpa qui officia deserunt mollit anim id est laborum</p>
    <div class="confidential">Proprietary and Confidential</div>
    <div class="brand-mark">Stovewise</div>
  </div>
</section>

<section class="slide slide--dark col-2 row-2">
  <div class="tagline">Cook. Learn. Repeat.</div>
  <div class="page-no">4</div>
  <h2 class="headline section-title" style="top:30px;font-size:26px">Consumer</h2>
  <h2 class="headline section-title" style="top:64px;font-size:42px">Insights</h2>
  <div class="confidential">Proprietary and Confidential</div>
</section>

<section class="slide col-3 row-2">
  <div class="rail"></div>
  <div class="tagline">Cook. Learn. Repeat.</div>
  <div class="page-no">5</div>
  <div class="kicker insight-kicker">Insight 1</div>
  <h3 class="headline insight-title" style="top:33px">Growing<br>Interest<br><span class="accent">in Virtual<br>Cooking Classes</span></h3>
  <div class="divider-v" style="left:212px;top:31px;height:134px"></div>
  <p class="copy insight-body" style="top:55px">Consumers seeking alternatives, more choices, easier preference management, or simply a way to avoid crowded spaces are increasingly turning to online culinary education platforms. This trend is fueled by the desire to learn new cooking skills, explore different cuisines, and enjoy cooking as a leisure activity or a bonding experience with friends and family, even if remotely</p>
  <div class="confidential">Proprietary and Confidential</div>
  <div class="brand-mark">Stovewise</div>
</section>

<section class="slide col-1 row-3">
  <div class="rail"></div>
  <div class="tagline">Cook. Learn. Repeat.</div>
  <div class="page-no">6</div>
  <div class="kicker insight-kicker">Insight 1</div>
  <h3 class="headline insight-title" style="top:33px">Demand for<br>Interactive<br>and<br><span class="accent">Personalized<br>Experience</span></h3>
  <div class="divider-v" style="left:212px;top:31px;height:134px"></div>
  <p class="copy insight-body" style="top:73px">Consumers value interactive and personalized virtual cooking experiences. This includes live classes with real-time feedback from chefs, personalized meal planning, and customization options that cater to dietary restrictions or preferences. Platforms that offer these personalized interactions tend to be more popular.</p>
  <div class="confidential">Proprietary and Confidential</div>
  <div class="brand-mark">Stovewise</div>
</section>

<section class="slide col-2 row-3">
  <div class="rail"></div>
  <div class="tagline">Cook. Learn. Repeat.</div>
  <div class="page-no">7</div>
  <div class="kicker insight-kicker">Insight 1</div>
  <h3 class="headline insight-title" style="top:33px">Global<br>Cuisine<br><span class="accent">Exploration</span></h3>
  <div class="divider-v" style="left:212px;top:31px;height:134px"></div>
  <p class="copy insight-body" style="top:63px">There is a marked interest in exploring global cuisines through virtual cooking classes. Consumers are eager to learn about and experiment with dishes from different cultures, driven by a desire for new experiences and flavors. This trend is facilitated by the accessibility of virtual classes, which can connect chefs and culinary instructors from around the world with interested learners.</p>
  <div class="confidential">Proprietary and Confidential</div>
  <div class="brand-mark">Stovewise</div>
</section>

<section class="slide slide--dark col-3 row-3">
  <div class="tagline">Cook. Learn. Repeat.</div>
  <div class="page-no">8</div>
  <h2 class="headline section-title" style="top:32px;font-size:26px">The</h2>
  <h2 class="headline section-title" style="top:66px;font-size:43px">Problem</h2>
  <div class="confidential">Proprietary and Confidential</div>
</section>

<section class="slide col-1 row-4" style="background:var(--paper)">
  <div class="problem-panel">
    <p class="copy problem-item" style="top:23px">Lorem ipsum dolor sit amet, consectetur adipiscing elit, sed do eiusmod tempor incididunt ut labore et dolore magna aliqua. Ut enim ad minim veniam, quis nostrud exercitation ullamco laboris nisi ut aliquip ex ea commodo consequat.</p>
    <p class="copy problem-item" style="top:95px">Lorem ipsum dolor sit amet, consectetur adipiscing elit, sed do eiusmod tempor incididunt ut labore et dolore magna aliqua. Ut enim ad minim veniam, quis nostrud exercitation ullamco laboris nisi ut aliquip ex ea commodo consequat.</p>
  </div>
  <div class="tagline">Cook. Learn. Repeat.</div>
  <div class="page-no">9</div>
  <h2 class="headline problem-title">The<br>Problem</h2>
  <div class="confidential">Proprietary and Confidential</div>
  <div class="brand-mark">Stovewise</div>
</section>

<section class="slide slide--dark col-2 row-4">
  <div class="tagline">Cook. Learn. Repeat.</div>
  <div class="page-no">10</div>
  <h2 class="headline section-title" style="top:32px;font-size:26px">Market</h2>
  <h2 class="headline section-title" style="top:66px;font-size:43px">Opportunity</h2>
  <div class="confidential">Proprietary and Confidential</div>
</section>

<section class="slide col-3 row-4">
  <div class="rail"></div>
  <div class="ci-top"></div>
  <div class="tagline">Cook. Learn. Repeat.</div>
  <div class="page-no">11</div>
  <div class="kicker ci-kicker">Consumer Insight 1</div>
  <h3 class="headline ci-title"><span class="accent">Increasing Demand for</span><br>Healthier Home-Cooked Meals</h3>
  <div class="divider-h" style="left:33px;top:103px;width:68px"></div>
  <p class="copy ci-body">Lorem ipsum dolor sit amet, consectetur adipiscing elit, sed do eiusmod tempor incididunt ut labore et dolore magna aliqua. Ut enim ad minim veniam, quis nostrud exercitation ullamco laboris nisi ut aliquip ex ea commodo consequat. Duis aute irure dolor in reprehenderit in voluptate velit esse cillum dolore eu fugiat nulla pariatur. Excepteur sint occaecat cupidatat non proident, sunt in culpa qui officia deserunt mollit anim id est laborum</p>
  <div class="confidential">Proprietary and Confidential</div>
  <div class="brand-mark">Stovewise</div>
</section>

<section class="slide col-1 row-5" style="left:47px">
  <div class="rail"></div>
  <div class="ci-top"></div>
  <div class="tagline">Cook. Learn. Repeat.</div>
  <div class="page-no">12</div>
  <div class="kicker ci-kicker">Consumer Insight 2</div>
  <h3 class="headline ci-title"><span class="accent">Convenience and</span><br>Time-Saving Solutions</h3>
  <div class="divider-h" style="left:33px;top:104px;width:68px"></div>
  <p class="copy" style="position:absolute;left:119px;top:100px;width:184px">Another key insight is the high demand for convenience and time-saving solutions, particularly among busy households and individuals with fast-paced lifestyles. Lorem ipsum dolor eset Lorem ipsum dolor eset Lorem ipsum dolor eset Lor Lorem ipsum dolor eset Lorem ipsum dolor</p>
  <div class="confidential">Proprietary and Confidential</div>
  <div class="brand-mark">Stovewise</div>
</section>

<section class="slide slide--dark col-2 row-5">
  <div class="tagline">Cook. Learn. Repeat.</div>
  <div class="page-no">13</div>
  <h2 class="headline section-title" style="top:22px;font-size:26px">Current</h2>
  <h2 class="headline section-title" style="top:56px;font-size:43px">Solutions</h2>
  <div class="confidential">Proprietary and Confidential</div>
</section>

<section class="slide col-3 row-5" style="background:var(--paper)">
  <div class="tagline">Cook. Learn. Repeat.</div>
  <div class="page-no">14</div>
  <div class="comp-col" style="left:28px">
    <div class="comp-name"><span class="dot"></span>Tutorline</div>
    <p class="comp-copy">Tutorline, a leader in online prerecorded learning, offers celebrity-taught video courses across various subjects. Their high production value and renowned instructors have made them a powerhouse in the premium learning space. This success reflects the vibrancy of the online education market.</p>
    <div class="comp-label">Estimated Valuation:</div>
    <div class="comp-value">$2.7B</div>
  </div>
  <div class="comp-col" style="left:135px;background:#ebebee">
    <div class="comp-name">Kitchen Avenue</div>
    <p class="comp-copy">Kitchen Avenue was a prominent player in the high-end kitchenware and cooking class space. They offered in-store shopping experiences with premium cookware and ingredients, alongside engaging cooking classes led by culinary professionals.</p>
    <div class="comp-label">Estimated Valuation:</div>
    <div class="comp-value">$50M</div>
  </div>
  <div class="comp-col" style="left:242px;width:104px">
    <div class="comp-name" style="color:var(--ember)">Hearthbook</div>
    <p class="comp-copy">Hearthbook, another player in the online culinary education space, provides in-person and online cooking classes with a focus on connecting users with local chefs. They offer a variety of class formats, from group courses to private chef experiences.</p>
    <div class="comp-label">Estimated Valuation:</div>
    <div class="comp-value">$2.6M</div>
  </div>
  <p class="takeaway"><b>Key Takeaway:</b> Lorem ipsum dolor sit amet, consectetur adipiscing elit, sed do eiusmod tempor incididunt ut labore et dolore magna aliqua. Ut enim ad minim veniam, quis nostrud exercitation ullamco laboris nisi ut aliquip ex ea commodo consequat. Duis aute irure dolor in reprehenderit in voluptate velit esse cillum dolore eu fugiat nulla pariatur.</p>
  <div class="confidential">Proprietary and Confidential</div>
  <div class="brand-mark">Stovewise</div>
</section>

</body>
</html>
```